Artisan Bread Company needs a business card

I need a business card design, for an artisan bread company called "Hollin's Bread".

I would like the logo on one side, and on the other, I would like it to say

Tavish Hollin
Baker
519.362.4175
hollinsbread@mailvexo.com

Not necessarily in that order- but it must have these.

Industry/Entity Type

Business

Font styles to use
Serif

Requirements
Must have
• The provided logo on the front, this on the back-
• Tavish Hollin
• Baker
• 519.362.4175
• hollinsbread@mailvexo.com

```html
<!DOCTYPE html>
<html lang="en">
<head>
<meta charset="utf-8">
<title>Hollin's Bread — Business Card</title>
<link rel="stylesheet" href="https://fonts.googleapis.com/css2?family=Jost:wght@300;400;600&display=swap">
<style>
  :root {
    --backdrop: #e9e6e1;
    --card-light: #ffffff;
    --card-dark: #2a2a2a;
    --ink: #1f1f1f;
    --ink-soft: #3a3a3a;
    --rule: #4a4a4a;
    --paper-text: #ffffff;
    --shadow: rgba(0, 0, 0, 0.18);
  }
  * { margin: 0; padding: 0; box-sizing: border-box; }
  html, body {
    width: 1200px;
    height: 800px;
    overflow: hidden;
    background: var(--backdrop);
    font-family: "Jost", "Futura", sans-serif;
  }
  .canvas {
    position: relative;
    width: 1200px;
    height: 800px;
  }
  .card {
    position: absolute;
    left: 302px;
    width: 596px;
    height: 340px;
    border-radius: 16px;
    box-shadow: 0 6px 18px var(--shadow);
    display: flex;
    flex-direction: column;
    align-items: center;
    justify-content: center;
  }
  .card--details {
    top: 40px;
    background: var(--card-light);
    color: var(--ink);
  }
  .card--brand {
    top: 420px;
    background: var(--card-dark);
    color: var(--paper-text);
  }
  .person-name {
    font-weight: 600;
    font-size: 25px;
    letter-spacing: 1.5px;
    text-transform: uppercase;
  }
  .person-role {
    font-weight: 300;
    font-size: 17px;
    color: var(--ink-soft);
    margin-top: 2px;
    letter-spacing: 0.5px;
  }
  .divider {
    width: 150px;
    height: 1px;
    background: var(--rule);
    margin: 22px 0 20px;
  }
  .contact-line {
    font-weight: 300;
    font-size: 18px;
    line-height: 1.3;
    letter-spacing: 0.3px;
  }
  .brand-name {
    font-weight: 400;
    font-size: 46px;
    letter-spacing: 1px;
  }
</style>
</head>
<body>
  <main class="canvas">
    <section class="card card--details" aria-label="Card front with contact details">
      <h1 class="person-name">Tavish Hollin</h1>
      <p class="person-role">Baker</p>
      <div class="divider"></div>
      <p class="contact-line">519.362.4175</p>
      <p class="contact-line">hollinsbread@mailvexo.com</p>
    </section>
    <section class="card card--brand" aria-label="Card back with company name">
      <p class="brand-name">Hollin's Bread</p>
    </section>
  </main>
</body>
</html>
```